Brochure Design Project

We are a payroll company. We offer a wide variety of products and services:
1. Payroll Processing
2. Employee Direct Deposit
3. Time and attendance
4. HR services
5. Employee Employee Benefits

I'd like to develop a one page template that uses a combination of our logo (attached), colors (attached) and possible a picture. The picture could be shown as an option as it may change based on the product or service.

Target Market(s)

Adults in the United States ages 22-50. Typically these people are accountants, human resource professionals or entrepreneurs. The payroll industry is dominated by 3 large payroll processors, KLV, Wendorn and Tolvaris. These companies are very impersonal and make it difficult to resolve issues when they arise. We have grown to over 400 clients by being the opposite of the big guys,

Industry/Entity Type

It Company

Font styles to use
Sans Serif

Requirements
Must have
• The brochure can be one or two pages.
Nice to have
• I'll know it when I see it but I can't describe it. I have attached a few brochures that have caught my eye.
Should not have
• No cartoons. No money signs. Hip, new, fresh are words I'd use to describe the winning product. Of the three people I described in my target market, the entrepreneur is the market I'd most like to target.

```html
<!DOCTYPE html>
<html lang="en">
<head>
<meta charset="utf-8">
<title>Paywell Partners – Brochure Front &amp; Back</title>
<link href="https://fonts.googleapis.com/css2?family=Source+Sans+3:wght@300;400;600&display=swap" rel="stylesheet">
<style>
  :root{
    --board:#ffffff;
    --slate:#6b6e71;
    --slate-light:#c9cbcd;
    --leaf:#8dc63f;
    --leaf-pale:#c7e29c;
    --leaf-mist:#d9ecbd;
    --band-start:#4cb848;
    --band-end:#0f7d6e;
    --teal-text:#17806f;
    --navy:#1d2f6f;
    --caption:#a7a9ac;
    --ink:#2f3a2b;
    --white:#ffffff;
  }
  *{box-sizing:border-box;margin:0;padding:0}
  html,body{width:1200px;height:848px;overflow:hidden;background:var(--board)}
  body{position:relative;font-family:"Source Sans 3",Arial,sans-serif}

  .panel{position:absolute;overflow:hidden;border-radius:0 0 16px 16px}

  /* Front */
  .front{left:179px;top:122px;width:424px;height:564px;background:var(--slate)}
  .front-photo{position:absolute;left:0;top:0;width:424px;height:220px;
    background:linear-gradient(135deg,#d9c9a0 0%,#b39b68 45%,#7a6a45 100%)}
  .front-band{position:absolute;left:0;top:220px;width:424px;height:73px;
    background:linear-gradient(90deg,var(--band-start),var(--band-end));overflow:hidden}
  .front-band .tagline{position:absolute;left:36px;top:4px;color:var(--white);
    font-weight:300;font-size:20px}
  .front-band .value-word{position:absolute;left:198px;top:-22px;color:rgba(255,255,255,.3);
    font-weight:300;font-size:108px;line-height:1;letter-spacing:-1px}
  .quote{position:absolute;left:26px;top:312px;width:306px;color:var(--slate-light);
    font-weight:300;font-size:16.5px;line-height:18px}
  .quote cite{display:block;text-align:right;font-style:normal;font-size:11px;margin-top:2px}
  .front .brand{position:absolute;right:24px;bottom:30px;color:var(--white);
    font-weight:600;font-size:15px;text-align:right;line-height:16px}

  /* Back */
  .back{left:624px;top:123px;width:424px;height:572px;background:var(--leaf)}
  .back-photo{position:absolute;left:0;top:0;width:424px;height:217px;
    background:linear-gradient(120deg,#2f5f8e 0%,#7fb3dc 45%,#c5dcec 65%,#5d8f3a 85%,#3f6d28 100%)}
  .back-title{position:absolute;left:50px;top:232px;color:var(--white);
    font-weight:300;font-size:19px;line-height:21px}
  .info-box{position:absolute;left:27px;top:286px;width:369px;height:173px;
    background:var(--leaf-pale);border-radius:14px 14px 0 0}
  .services{text-align:center;color:var(--teal-text);font-weight:400;font-size:11px;line-height:13px;margin-top:10px}
  .cols{display:flex;gap:10px;padding:7px 10px 0 11px}
  .cols .col{font-size:7.6px;line-height:8.3px;color:var(--ink)}
  .cols .col:first-child{width:170px}
  .cols .col:last-child{flex:1}
  .cols p{margin-bottom:4px}
  .promo{color:var(--teal-text);font-size:12.5px !important;line-height:13px;margin-top:6px}
  .contact{position:absolute;left:51px;top:490px;color:var(--white);font-weight:300;
    font-size:12.5px;line-height:13.5px}
  .contact .address{font-size:7.5px;margin-top:5px;opacity:.9}
  .logo-stage{position:absolute;left:256px;top:470px;width:150px;height:92px}
  .logo-stage .back-square{position:absolute;background:var(--leaf-mist);opacity:.6}
  .logo-stage .card{position:absolute;left:22px;top:19px;width:113px;height:60px;background:var(--white);
    display:flex;align-items:center;justify-content:center;text-align:center;
    color:var(--navy);font-weight:600;font-size:14px;line-height:15px}

  .caption{position:absolute;left:179px;top:694px;color:var(--caption);font-weight:300;font-size:14px}
  .board-brand{position:absolute;right:50px;top:760px;color:var(--navy);font-weight:600;
    font-size:18px;line-height:19px;text-align:right}
</style>
</head>
<body>

<section class="panel front">
  <div class="front-photo" role="img" aria-label="Close-up of a banknote portrait under a fine grid, warm sepia tones"></div>
  <div class="front-band">
    <span class="value-word">value</span>
    <span class="tagline">Innovative solutions that deliver</span>
  </div>
  <blockquote class="quote">
    "Associate yourself with men of good quality if you esteem your own reputation; for 'tis better to be alone than in bad company."
    <cite>Harlan Whitcombe.</cite>
  </blockquote>
  <div class="brand">Paywell<br>Partners</div>
</section>

<section class="panel back">
  <div class="back-photo" role="img" aria-label="Glass office facade with diagonal frames reflecting blue sky beside green foliage"></div>
  <h1 class="back-title">Integrated Employer Solutions That<br>Create Value for Your Business</h1>
  <div class="info-box">
    <p class="services">Payroll Processing • Employee Direct Deposit • Time and attendance<br>HR services • Employee Employee Benefits</p>
    <div class="cols">
      <div class="col">
        <p>Paywell Partners serves as an administrative services organization offering comprehensive payroll management, HR solutions and benefits administration for your business.</p>
        <p>While our premier service for 20+ years has been payroll, we have evolved to accommodate our clients' needs and developed a unique combination of innovative employer solutions supported by client-focused professionals. The result is a highly personalized, strategic relationship dedicated to your business success.</p>
      </div>
      <div class="col">
        <p>If you are looking for an ASO that offers a flexible, integrated suite of services delivered with outstanding customer attention you have come to the right place!</p>
        <p>With a 98% client retention rate, our statistics speak for themselves!</p>
        <p class="promo">Ready to relax about payroll?<br>Learn about our free payroll<br>promotion for 2014!</p>
      </div>
    </div>
  </div>
  <div class="contact">
    T: 555-014-2281<br>
    F: 555-014-2290<br>
    E: jcarver@paywellpartners.example
    <div class="address">Address: 88 North Elm Avenue, Suite 310 • Brookfield PA • 19999</div>
  </div>
  <div class="logo-stage">
    <div class="back-square" style="left:0;top:10px;width:150px;height:80px"></div>
    <div class="back-square" style="left:14px;top:0;width:124px;height:92px"></div>
    <div class="card">Paywell<br>Partners</div>
  </div>
</section>

<p class="caption">Brochure Visual - Front &amp; Back</p>
<div class="board-brand">Paywell<br>Partners</div>

</body>
</html>
```